Invitation annual meeting 2017 of Corvelle Group (2017 Annual Staff Appointments)

Version française: We want to create an invitation to the annual meeting of Groupe Corvelle. This invitation will also be printed as a poster. You will find enclosed a photo of a "B" made with the employees of the Group during an internal event. You will absolutely have this photo on the invitation. I also send it to you when you save it while waiting for the invitation. The invitation must be festive, elegant and classy, ​​because it will take place on the 18th of December, just before Christmas (on the theme of Christmas and New Year Eve). Please, do not use the color "red" on this invitation. You can use this gray: Pantone 431 C for this invitation if you want to. The annual meeting of the staff (annual meeting) 18 December 2017 (18th) of December 2017) Marlindôme (at Marlindome) From 5pm to 9.30pm (from 5pm to 9.30pm) French version: On the occasion of the annual meeting of the staff we wish to make an invitation which will also be printed as a poster. You will find in the attached elements a photo of a B made on the beach with employees. It will be necessary to use this B imperatively for your creation. I am also sending you the quick save the date we had done while waiting for the invitation. This one must be classy, ​​festive because the event will take place on December 18th, with the approach of the end-of-year celebrations (thematic New Year's Eve and non-christmas). You can use anthracite gray: Pantone 431C The group logo should appear on the invitation. Text: Annual Staff Meeting 18 December 2017 Marlindôme from 5pm to 9.30pm
Updates

Project Deadline Extended Reason: Hello We give two more days on the project because we have not been fully seduced by the proposals received so far. Added Tuesday, October 24, 2017

Target Market(s)

ENG: Internal ==> employees of the Corvelle Group FR: internal to the Group

Colors

Requirements
Must have
• ENG: It is obligatory to use the photo of the "B" on the beach for this invitation. You can crop the image of the B if you want to. FR: B "made by employees" of the transmitted photo (possibility of detaching it)
Should not have
• ENG: Boat photos, "kitsch" designs and the color red EN: the pictures of boats, the "kitsch", the red

```html
<!DOCTYPE html>
<html lang="fr">
<head>
<meta charset="UTF-8">
<title>Rendez-vous annuel du personnel — Groupe Corvelle</title>
<link rel="stylesheet" href="https://fonts.googleapis.com/css2?family=Anton&family=Lato:wght@400;900&family=Montserrat:wght@500;800;900&display=swap">
<style>
  :root {
    --paper: #f7f7f8;
    --paper-shade: #e9e9ec;
    --ornament-grey: #c9c9cc;
    --logo-slate: #3b4757;
    --navy: #0e2c48;
    --deep-teal: #0b3040;
    --slate-blue: #2b4865;
    --teal: #1b9b97;
    --splash-top: #0f4f80;
    --splash-mid: #1ca7b2;
    --splash-low: #7fcfc6;
    --splash-sand: #efe8d9;
    --sand: #c6a888;
    --sand-light: #d9c3a6;
    --white: #ffffff;
  }
  * { margin: 0; padding: 0; box-sizing: border-box; }
  html, body { width: 950px; height: 1200px; overflow: hidden; background: var(--paper); }
  .poster {
    position: relative;
    width: 950px;
    height: 1200px;
    overflow: hidden;
    background: linear-gradient(180deg, var(--paper) 0%, #fdfdfd 50%, var(--paper-shade) 100%);
    font-family: "Montserrat", sans-serif;
  }
  .floral-backdrop {
    position: absolute;
    left: 0; top: 70px;
    width: 950px; height: 940px;
    background: radial-gradient(ellipse at 50% 50%, rgba(190,190,194,.55) 0%, rgba(205,205,208,.35) 45%, rgba(247,247,248,0) 72%);
  }
  .brand {
    position: absolute;
    top: 62px; left: 0; width: 950px;
    text-align: center;
    font-family: "Montserrat", sans-serif;
    font-weight: 500;
    font-size: 28px;
    letter-spacing: 7px;
    color: var(--logo-slate);
  }
  .splash {
    position: absolute;
    left: 80px; top: 245px;
    width: 760px; height: 590px;
  }
  .frame { position: absolute; left: 0; top: 0; width: 950px; height: 1200px; }
  .title { position: absolute; white-space: nowrap; line-height: 1; }
  .title--rendez {
    left: 212px; top: 312px;
    font-weight: 900; font-size: 104px; color: var(--navy);
    letter-spacing: -1px;
  }
  .title--vous {
    left: 226px; top: 420px;
    font-weight: 900; font-size: 132px; color: var(--white);
    letter-spacing: -2px;
  }
  .title--annuel {
    left: 210px; top: 545px;
    font-family: "Anton", sans-serif; font-size: 134px; color: var(--deep-teal);
    letter-spacing: -1px;
  }
  .title--du {
    left: 592px; top: 556px;
    width: 110px; height: 110px;
    font-family: "Anton", sans-serif; font-size: 104px; color: var(--deep-teal);
    transform-origin: 0 0;
    transform: translate(112px, 0) rotate(90deg);
  }
  .title--personnel {
    left: 212px; top: 682px;
    font-weight: 800; font-size: 70px; color: var(--slate-blue);
    letter-spacing: 1px;
  }
  .date-day {
    position: absolute; left: 62px; top: 905px;
    font-weight: 900; font-size: 174px; line-height: 1; color: var(--teal);
    letter-spacing: -4px;
  }
  .date-month {
    position: absolute; left: 70px; top: 1064px;
    font-weight: 800; font-size: 35px; line-height: 1; color: var(--sand);
    letter-spacing: -1px;
  }
  .date-year {
    position: absolute; left: 66px; top: 1095px;
    font-weight: 800; font-size: 74px; line-height: 1; color: var(--sand-light);
    letter-spacing: -1px;
  }
  .divider {
    position: absolute; left: 297px; top: 944px;
    width: 2px; height: 210px; background: var(--teal);
  }
  .venue {
    position: absolute; left: 326px; top: 1070px;
    font-family: "Lato", sans-serif; font-weight: 900; font-size: 41px; line-height: 1;
    color: var(--teal); white-space: nowrap;
  }
  .hours {
    position: absolute; left: 326px; top: 1117px;
    font-family: "Lato", sans-serif; font-weight: 400; font-size: 42px; line-height: 1;
    color: var(--sand); white-space: nowrap;
  }
  .staff-photo {
    position: absolute; left: 752px; top: 1032px;
    width: 140px; height: 88px;
    border-radius: 10px 14px 22px 8px;
    background: linear-gradient(135deg, #6d6fa0 0%, #9a5f8e 35%, #4f8fa8 65%, #8b8fb3 100%);
  }
</style>
</head>
<body>
<main class="poster">
  <div class="floral-backdrop" role="img" aria-label="Soft grey floral illustration with festive ornaments behind the title"></div>

  <div class="brand">GROUPE CORVELLE</div>

  <svg class="splash" viewBox="0 0 760 590" role="img" aria-label="Watercolour splash from deep blue through turquoise to sand">
    <defs>
      <linearGradient id="splashFill" x1="0" y1="0" x2="0" y2="1">
        <stop offset="0" stop-color="var(--splash-top)"/>
        <stop offset="0.35" stop-color="var(--splash-mid)"/>
        <stop offset="0.65" stop-color="var(--splash-low)"/>
        <stop offset="0.85" stop-color="var(--splash-sand)"/>
        <stop offset="1" stop-color="var(--splash-sand)"/>
      </linearGradient>
    </defs>
    <path fill="url(#splashFill)" d="M200 30 C320 0 520 10 640 40 C700 70 720 160 730 260 C745 370 720 470 660 540 C560 590 300 590 170 560 C90 530 60 440 60 340 C50 230 70 120 120 70 C150 45 175 38 200 30 Z"/>
  </svg>

  <svg class="frame" viewBox="0 0 950 1200" aria-hidden="true">
    <g fill="none" stroke="var(--white)" stroke-width="8">
      <polyline points="172,300 172,804 744,804 744,380"/>
      <line x1="172" y1="290" x2="190" y2="290"/>
    </g>
    <polygon points="385,285 600,285 590,297 395,297" fill="var(--white)"/>
  </svg>

  <div class="title title--rendez">RENDEZ-</div>
  <div class="title title--vous">VOUS</div>
  <div class="title title--annuel">ANNUEL</div>
  <div class="title title--du">DU</div>
  <div class="title title--personnel">PERSONNEL</div>

  <div class="date-day">18</div>
  <div class="date-month">DÉCEMBRE</div>
  <div class="date-year">2017</div>
  <div class="divider"></div>
  <div class="venue">AU MARLINDÔME</div>
  <div class="hours">DE 17H À 21H30</div>

  <div class="staff-photo" role="img" aria-label="Photo of employees forming a large letter on the beach"></div>
</main>
</body>
</html>
```